Visitenkarten für Psychotherapeutin
Zielgruppe
Ich war Psychologin und Coachin und bin jetzt eine approbierte Psychotherapeutin.
Aufgabenstellung
Es gibt ein Layout, an das sich angelehnt werden soll.
Die Farb- und Schriftwelt liegt vor, jedoch soll aus dem türkies ein warmer Pink-Rot-Ton werden.
Die Visitenkarte soll für die neu eröffnete Privatpraxis verwendet werden. Im Logo soll die Berufsbezeichnung Psychologische Psychotherapeutin (mit) Schwerpunkt Systemische Therapie stehen.
Neben den Kontaktdaten folgender Text:
Privatpraxis für Psychologische Psychotherapie, Schwerpunkt Systemische Therapie
Für Privatversicherte und Selbstzahlende
Termin nach Vereinbarung
Die Zeile mit der Sprechstunde soll weg.

```html
<!DOCTYPE html>
<html lang="de">
<head>
<meta charset="utf-8">
<title>Visitenkarte Korinna Welse</title>
<link rel="stylesheet" href="https://fonts.googleapis.com/css2?family=Montserrat:wght@300;400;600;700&display=swap">
<style>
  :root {
    --page-bg: #f7f7f7;
    --brand-red: #e05263;
    --brand-text: #c9495a;
    --card-white: #ffffff;
    --on-brand: #ffffff;
  }
  html, body {
    margin: 0;
    padding: 0;
    width: 1200px;
    height: 2359px;
    overflow: hidden;
    background: var(--page-bg);
    font-family: "Montserrat", Arial, sans-serif;
  }
  .canvas {
    position: relative;
    width: 1200px;
    height: 2359px;
  }
  .card-front {
    position: absolute;
    left: 0;
    top: 781px;
    width: 1200px;
    height: 776px;
    background: var(--brand-red);
    color: var(--on-brand);
  }
  .wordmark {
    position: absolute;
    left: 127px;
    top: 1040px;
    margin: 0;
    font-weight: 600;
    font-size: 112px;
    line-height: 1;
    letter-spacing: 1px;
    color: var(--on-brand);
    top: 200px;
  }
  .profession {
    position: absolute;
    left: 127px;
    top: 448px;
    margin: 0;
    font-weight: 700;
    font-size: 22px;
    letter-spacing: 4.3px;
    text-transform: uppercase;
  }
  .specialty {
    position: absolute;
    left: 127px;
    top: 482px;
    margin: 0;
    font-weight: 400;
    font-size: 22px;
    letter-spacing: 4.2px;
    text-transform: uppercase;
  }
  .card-back {
    position: absolute;
    left: 0;
    top: 1582px;
    width: 1172px;
    height: 775px;
    background: var(--card-white);
    border: 1px solid var(--brand-red);
    color: var(--brand-text);
  }
  .card-back .holder {
    position: absolute;
    left: 127px;
    top: 196px;
    margin: 0;
    font-weight: 600;
    font-size: 40px;
    line-height: 1;
  }
  .card-back .practice,
  .card-back .contact,
  .card-back .terms {
    position: absolute;
    left: 127px;
    margin: 0;
    font-weight: 400;
    font-size: 33px;
    line-height: 42px;
  }
  .card-back .practice { top: 240px; }
  .card-back .contact { top: 414px; }
  .card-back .terms { top: 624px; }
  .card-back a { color: inherit; text-decoration: none; }
</style>
</head>
<body>
<main class="canvas">
  <section class="card-front" aria-label="Vorderseite">
    <h1 class="wordmark">Korinna Welse</h1>
    <p class="profession">Psychologische Psychotherapeutin</p>
    <p class="specialty">Systemische Therapie</p>
  </section>

  <section class="card-back" aria-label="Rückseite">
    <h2 class="holder">KORINNA WELSE</h2>
    <p class="practice">Privatpraxis für Psychologische Psychotherapie,<br>Schwerpunkt Systemische Therapie</p>
    <p class="contact">
      Lindenhainweg 14 . 85640 Aubachfeld<br>
      T. +49 170 5550148<br>
      <a href="mailto:kontakt@hmorbachtu.de">kontakt@hmorbachtu.de</a><br>
      <a href="https://www.hmorbachtu.de">www.hmorbachtu.de</a>
    </p>
    <p class="terms">Für Privatversicherte und Selbstzahlende<br>Termin nach Vereinbarung</p>
  </section>
</main>
</body>
</html>
```